Medical Marijuana Potato Chip Bags Need Graphic Design

We are looking for a bag design for our new brand of medical marijuana potato chips. The design should be simple, the less colors used the better. We are looking for a classic kind of potato chip design somewhere between that of the bag design of Hollow Oak Potato Chips, Marnie's Pita Chips and Bluff Rock Potato Chips.

The main logo is "Golden Furrow Munchies" with "Potato Chips" written underneath it. The original idea was to have a simple sketch of a POTATO SMOKING A JOINT underneath the font, open to other ideas but that would be ideal. In terms of texture and color, we are very open but if you're lost use a burlap sack as influence

This is for the front and back so the design should be able to wrap around. Details such as nutrition info will be added later.
The dimensions are 10"x8" (that includes front and back) or two 5"x8" pictures (one for front, one for back).
Remember that it must appeal to the variety of patients using medical marijuana, from young adults with minor ailments to senior citizens with terminal diseases.

We've decided to make our project non-refundable so the best idea will be rewarded!

Reason: We are just waiting on a few more designs from designers who requested more time. Great job on all the designs so far!

```html
<!DOCTYPE html>
<html lang="en">
<head>
<meta charset="utf-8">
<title>Golden Furrow Munchies – Bag Front and Back</title>
<link rel="stylesheet" href="https://fonts.googleapis.com/css2?family=Arvo:wght@700&family=Libre+Baskerville:wght@400&family=Oswald:wght@600&display=swap">
<style>
  :root {
    --page: #ffffff;
    --burlap: #bcb29b;
    --burlap-edge: #a89e87;
    --cream: #efeadb;
    --dash: #7a5240;
    --leaf-light: #8fc97f;
    --leaf-dark: #2f5d2e;
    --banner-top: #86cb7c;
    --banner-bottom: #5aa655;
    --title: #ffffff;
    --gold: #e6a628;
    --gold-dark: #a27a1e;
    --seal-cream: #f6f1e2;
    --brown-text: #6b4a3a;
    --tag-start: #f9d77a;
    --tag-end: #e9a93a;
    --tag-text: #a13aa5;
  }
  * { box-sizing: border-box; margin: 0; padding: 0; }
  html, body { width: 1000px; height: 1200px; overflow: hidden; background: var(--page); }
  .canvas { position: relative; width: 1000px; height: 1200px; }

  .panel {
    position: absolute; top: 248px; width: 440px; height: 704px;
    background: var(--burlap);
    box-shadow: 0 2px 6px rgba(0,0,0,0.35);
    overflow: hidden;
  }
  .panel--front { left: 40px; }
  .panel--back { left: 520px; }

  .trim-band {
    position: absolute; left: 0; width: 100%; height: 58px;
    background: var(--cream);
  }
  .trim-band--top { top: 25px; }
  .trim-band--bottom { top: 632px; }
  .trim-band .dash-line {
    position: absolute; left: 12px; right: 12px; height: 0;
    border-top: 3px dashed var(--dash);
  }
  .trim-band--top .dash-line { top: 9px; }
  .trim-band--bottom .dash-line { bottom: 8px; }
  .leaf-row {
    position: absolute; left: 14px; right: 14px; height: 18px;
    background: linear-gradient(90deg, var(--leaf-light), #6fb55f, var(--leaf-light));
    border-radius: 9px; opacity: 0.85;
  }
  .trim-band--top .leaf-row { top: 25px; }
  .trim-band--bottom .leaf-row { top: 10px; }

  .new-tag {
    position: absolute; left: 0; top: 97px; width: 100px; height: 42px;
    background: linear-gradient(90deg, var(--tag-start), var(--tag-end));
    font-family: "Oswald", sans-serif; font-weight: 600; font-size: 28px;
    color: var(--tag-text); line-height: 42px; padding-left: 18px; letter-spacing: 1px;
  }

  .leaf-cluster {
    position: absolute; left: 76px; top: 104px; width: 290px; height: 84px;
    background: radial-gradient(ellipse at 50% 100%, var(--leaf-dark) 0%, #3f7a3a 55%, rgba(95,166,85,0) 78%);
    border-radius: 50% 50% 0 0 / 90% 90% 0 0;
  }

  .title-banner {
    position: absolute; left: 0; top: 178px; width: 100%; height: 122px;
    background: linear-gradient(180deg, var(--banner-top), var(--banner-bottom));
    text-align: center; padding-top: 20px;
  }
  .brand-name {
    font-family: "Arvo", serif; font-weight: 700; color: var(--title);
    text-transform: uppercase; line-height: 1.1;
  }
  .brand-name .line-main { display: block; font-size: 37px; letter-spacing: 0.5px; }
  .brand-name .line-sub { display: block; font-size: 30px; letter-spacing: 1px; margin-top: 4px; }

  .seal { position: absolute; left: 106px; top: 320px; width: 228px; height: 228px; }

  .product-line {
    position: absolute; left: 0; top: 582px; width: 100%;
    display: flex; align-items: center; justify-content: center; gap: 14px;
    font-family: "Libre Baskerville", serif; font-size: 21px; color: var(--brown-text);
    letter-spacing: 1px;
  }
  .product-line .rule { width: 44px; height: 2px; background: var(--brown-text); }
  .net-weight {
    position: absolute; right: 12px; top: 610px;
    font-family: "Libre Baskerville", serif; font-size: 12px; color: var(--brown-text);
  }
</style>
</head>
<body>
<main class="canvas">

  <section class="panel panel--front" aria-label="Bag front">
    <div class="trim-band trim-band--top">
      <div class="dash-line"></div>
      <div class="leaf-row" role="img" aria-label="Row of small green leaf motifs"></div>
    </div>

    <div class="new-tag">NEW</div>

    <div class="leaf-cluster" role="img" aria-label="Cluster of green leaves rising above the title banner"></div>

    <div class="title-banner">
      <h1 class="brand-name">
        <span class="line-main">Golden Furrow</span>
        <span class="line-sub">Munchies</span>
      </h1>
    </div>

    <svg class="seal" viewBox="0 0 228 228" aria-hidden="false">
      <circle cx="114" cy="114" r="112" fill="var(--seal-cream)"/>
      <circle cx="114" cy="114" r="94" fill="var(--gold)"/>
      <circle cx="114" cy="114" r="86" fill="none" stroke="var(--gold-dark)" stroke-width="3"/>
      <circle cx="114" cy="114" r="72" fill="var(--seal-cream)"/>
      <circle cx="114" cy="114" r="50" fill="var(--leaf-dark)" role="img" aria-label="Green leaf illustration in the centre of the seal"/>
    </svg>

    <div class="product-line">
      <span class="rule"></span>
      <span>POTATO CHIPS</span>
      <span class="rule" style="visibility:hidden"></span>
    </div>
    <div class="net-weight">32.5g</div>

    <div class="trim-band trim-band--bottom">
      <div class="leaf-row" role="img" aria-label="Row of small green leaf motifs"></div>
      <div class="dash-line"></div>
    </div>
  </section>

  <section class="panel panel--back" aria-label="Bag back">
    <div class="trim-band trim-band--top">
      <div class="dash-line"></div>
      <div class="leaf-row" role="img" aria-label="Row of small green leaf motifs"></div>
    </div>
  </section>

</main>
</body>
</html>
```